Volto FieldBrew needs a professional, modern and athlete appealing label for a square bottle

We need a label design for a new sports beverage drink called Volto FieldBrew. Looking for label that covers the front and back of the bottle, with the back showing the attached nutritional label. dimensions are below. This fieldBrew will appeal to athletes and fitness enthusiast alike. product is all natural and made with pure cane sugar. no addictives, colorings or preservatives. there are three favors, so three separate colors/packaging will be needed but the same base design. Original which is black tea, lemon and pineapple are the 3 flavors. I would need the attached nutritional label incorporated into the label. Plastic Bottle Square : 2.4" Height : 7.3" Label panel: 4.6" Label panel area: 1.5" x 5" for one side

Target Market(s)

athletes and fitness enthusiast. both male and female between the ages of 13-35

Industry/Entity Type

It Professional

Requirements
Must have
• the name of the beverage Volto FieldBrew
• Made with real tea
• all natural
• Tea + Electrolytes

```html
<!DOCTYPE html>
<html lang="en">
<head>
<meta charset="utf-8">
<title>Volto FieldBrew — Bottle Labels</title>
<link href="https://fonts.googleapis.com/css2?family=Anton&family=Oswald:wght@400;500&family=Montserrat:ital,wght@1,700&display=swap" rel="stylesheet">
<style>
  :root {
    --canvas: #ffffff;
    --red-base: #e31e24;
    --red-stripe: #85201f;
    --red-figure: rgba(120, 20, 20, 0.55);
    --red-ink: #ffffff;
    --yellow-base: #ffed00;
    --yellow-stripe: #fff176;
    --yellow-figure: rgba(240, 220, 0, 0.75);
    --yellow-ink: #231f20;
  }
  * { margin: 0; padding: 0; box-sizing: border-box; }
  html, body {
    width: 1200px; height: 1000px; overflow: hidden;
    background: var(--canvas);
  }
  .canvas { position: relative; width: 1200px; height: 1000px; }

  .label {
    position: absolute; top: 243px;
    width: 485px; height: 513px; overflow: hidden;
  }
  .label--original { left: 70px; --ink: var(--red-ink); }
  .label--lemon { left: 645px; --ink: var(--yellow-ink); }

  .label__stripes { position: absolute; inset: 0; width: 100%; height: 100%; }

  .label__athlete {
    position: absolute; left: 90px; top: 215px;
    width: 290px; height: 300px;
    border-radius: 45% 50% 0 0;
  }
  .label--original .label__athlete { background: radial-gradient(ellipse at 50% 40%, var(--red-figure), rgba(120,20,20,0.15) 75%); }
  .label--lemon .label__athlete { background: radial-gradient(ellipse at 50% 40%, var(--yellow-figure), rgba(240,220,0,0.2) 75%); }

  .vertical {
    position: absolute;
    writing-mode: vertical-rl;
    transform: rotate(180deg);
    white-space: nowrap;
    color: var(--ink);
    text-align: center;
  }
  .product-name {
    left: 213px; top: 37px; height: 415px; width: 66px;
    font-family: "Anton", sans-serif;
    font-size: 62px; line-height: 66px;
    letter-spacing: 0.5px;
    text-transform: uppercase;
  }
  .tagline {
    font-family: "Oswald", sans-serif;
    font-weight: 500;
    font-style: italic;
    font-size: 22px; line-height: 24px;
    width: 24px; text-align: start;
  }
  .tagline--real-tea { left: 168px; top: 267px; height: 182px; }
  .tagline--natural { left: 168px; top: 40px; height: 84px; }
  .benefit {
    left: 291px; top: 160px; height: 194px; width: 20px;
    font-family: "Montserrat", sans-serif;
    font-weight: 700; font-style: italic;
    font-size: 15px; line-height: 20px;
    letter-spacing: 0.3px;
  }
  .volume {
    position: absolute; left: 210px; top: 468px; width: 70px;
    text-align: center;
    font-family: "Oswald", sans-serif;
    font-size: 17px; color: var(--ink);
  }
</style>
</head>
<body>
<div class="canvas">

  <section class="label label--original">
    <svg class="label__stripes" viewBox="0 0 485 513" aria-hidden="true">
      <defs>
        <pattern id="stripes-original" width="84" height="84" patternUnits="userSpaceOnUse" patternTransform="rotate(-14)">
          <rect width="84" height="84" fill="var(--red-base)"/>
          <rect width="42" height="84" fill="var(--red-stripe)"/>
        </pattern>
      </defs>
      <rect width="485" height="513" fill="url(#stripes-original)"/>
    </svg>
    <div class="label__athlete" role="img" aria-label="Silhouette of a flexing athlete in darker red tones"></div>
    <p class="vertical tagline tagline--natural">all natural</p>
    <p class="vertical tagline tagline--real-tea">made with real tea</p>
    <h1 class="vertical product-name">Volto FieldBrew</h1>
    <p class="vertical benefit">TEA + ELECTROLYTES</p>
    <p class="volume">16 fl oz.</p>
  </section>

  <section class="label label--lemon">
    <svg class="label__stripes" viewBox="0 0 485 513" aria-hidden="true">
      <defs>
        <pattern id="stripes-lemon" width="84" height="84" patternUnits="userSpaceOnUse" patternTransform="rotate(-14)">
          <rect width="84" height="84" fill="var(--yellow-base)"/>
          <rect width="42" height="84" fill="var(--yellow-stripe)"/>
        </pattern>
      </defs>
      <rect width="485" height="513" fill="url(#stripes-lemon)"/>
    </svg>
    <div class="label__athlete" role="img" aria-label="Silhouette of a flexing athlete in yellow tones"></div>
    <p class="vertical tagline tagline--natural">all natural</p>
    <p class="vertical tagline tagline--real-tea">made with real tea</p>
    <h2 class="vertical product-name">Volto FieldBrew</h2>
    <p class="vertical benefit">TEA + ELECTROLYTES</p>
    <p class="volume">16 fl oz.</p>
  </section>

</div>
</body>
</html>
```